Product flyer with pricing

We manufacture iconic and luxury vending trailers. for our first trailer we need a flyer created to give to prospective clients with base pricing. I am uploading an example along with graphic files.

```html
<!DOCTYPE html>
<html lang="en">
<head>
<meta charset="utf-8">
<title>Pine Farm House Mini – Bright Roof Builds</title>
<link href="https://fonts.googleapis.com/css2?family=Oswald:wght@500;600;700&family=Questrial&display=swap" rel="stylesheet">
<style>
  :root {
    --yellow: #fbdb0a;
    --teal: #2e9bb8;
    --navy: #1b1160;
    --ink: #1c1c1c;
    --white: #ffffff;
    --photo-a: #e9eef2;
    --photo-b: #b8c4cc;
  }
  html, body { margin: 0; padding: 0; overflow: hidden; }
  body { width: 928px; height: 1200px; }
  .flyer {
    position: relative;
    width: 928px;
    height: 1200px;
    background: var(--yellow);
    overflow: hidden;
    font-family: "Questrial", sans-serif;
    color: var(--ink);
  }
  .backdrop { position: absolute; inset: 0; }
  .hero-photo {
    position: absolute;
    left: 33px; top: 113px;
    width: 497px; height: 460px;
    border-radius: 10px;
    background: linear-gradient(160deg, var(--white), var(--photo-a) 55%, var(--photo-b));
  }
  .brand {
    position: absolute;
    left: 640px; top: 120px;
    width: 220px;
    text-align: center;
    font-family: "Oswald", sans-serif;
    font-weight: 600;
    font-size: 30px;
    line-height: 34px;
    letter-spacing: 1px;
    color: var(--navy);
  }
  .title {
    position: absolute;
    left: 514px; top: 243px;
    margin: 0;
    font-family: "Oswald", sans-serif;
    font-weight: 700;
    font-size: 66px;
    line-height: 64px;
    color: var(--navy);
    text-transform: uppercase;
    letter-spacing: -0.5px;
  }
  .tagline {
    position: absolute;
    left: 515px; top: 438px;
    margin: 0;
    font-family: "Oswald", sans-serif;
    font-weight: 600;
    font-size: 25px;
    color: var(--navy);
  }
  .price-band {
    position: absolute;
    left: 508px; top: 504px;
    width: 420px; height: 61px;
    background: var(--teal);
    border-radius: 31px 0 0 31px;
    display: flex; align-items: center;
    padding-left: 30px;
    box-sizing: border-box;
    font-family: "Oswald", sans-serif;
    font-weight: 600;
    font-size: 38px;
    color: var(--yellow);
  }
  .thumb {
    position: absolute;
    left: 132px;
    width: 164px; height: 164px;
    box-sizing: border-box;
    border: 8px solid var(--white);
    border-radius: 30px;
    background: linear-gradient(180deg, #6fa9e0 0%, #dfe6ea 40%, #f4f6f7 70%, #3a3d40 100%);
  }
  .thumb--front { top: 613px; }
  .thumb--side { top: 794px; }
  .thumb--angle { top: 976px; }
  .section-title {
    position: absolute;
    left: 342px;
    margin: 0;
    font-family: "Oswald", sans-serif;
    font-weight: 600;
    font-size: 20px;
    color: var(--ink);
  }
  .features-title { top: 614px; }
  .options-title { top: 930px; }
  .spec-list {
    position: absolute;
    left: 342px;
    margin: 0; padding: 0;
    list-style: none;
    font-size: 19.5px;
    line-height: 25.5px;
  }
  .spec-list li { position: relative; padding-left: 27px; }
  .spec-list li::before {
    content: "";
    position: absolute;
    left: 3px; top: 9px;
    width: 8px; height: 8px;
    border-radius: 50%;
    background: var(--ink);
  }
  .features { top: 641px; width: 480px; }
  .options { top: 958px; width: 470px; }
  .options li { display: grid; grid-template-columns: 230px 18px auto; }
  .options .dash { text-align: center; }
</style>
</head>
<body>
<main class="flyer">
  <svg class="backdrop" width="928" height="1200" viewBox="0 0 928 1200" aria-hidden="true">
    <path fill="var(--teal)" d="M0 0 H657 C610 90 560 130 480 160 C400 250 380 470 340 565 C300 630 220 660 150 700 C90 760 50 860 0 896 Z"/>
  </svg>

  <div class="hero-photo" role="img" aria-label="White board-and-batten vending trailer on a tandem-axle chassis with an open serving window"></div>

  <div class="brand">BRIGHT ROOF<br>BUILDS</div>

  <h1 class="title">The<br>“Pine Farm<br>House Mini”</h1>
  <p class="tagline">Luxury, mobile vending house</p>

  <div class="price-band">Base Price: $ 45,000</div>

  <div class="thumb thumb--front" role="img" aria-label="Front view of the trailer with black door and window"></div>
  <div class="thumb thumb--side" role="img" aria-label="Side view of the trailer with shingled roof and upper windows"></div>
  <div class="thumb thumb--angle" role="img" aria-label="Three-quarter view of the trailer parked on a lot"></div>

  <h2 class="section-title features-title">Base unit features:</h2>
  <ul class="spec-list features">
    <li>Trailer features tandem wheels w/ brakes</li>
    <li>Steel frame construction for fire retardation safety and weight reduction.</li>
    <li>100% off grid with solar and lithium battery system allowing the trailer to be used in places not accessible by traditional trailers.</li>
    <li>80 gallon water supply tank</li>
    <li>100 gallon waste water tank</li>
    <li>Cupboards, cabinets &amp; four stainless steel sinks.</li>
    <li>60” Gas shock serving window</li>
  </ul>

  <h2 class="section-title options-title">Available options:</h2>
  <ul class="spec-list options">
    <li><span>HVAC - Kelvo Mini Split</span><span class="dash">-</span><span>$ 1,800</span></li>
    <li><span>Cooler / Glass front<br>Commercial refrigerator</span><span class="dash"><br>-</span><span><br>$ 1,600</span></li>
    <li><span>Upper loft storage area</span><span class="dash">-</span><span>$ 1,200</span></li>
    <li><span>Signage and graphics<br>depend on complexity</span><span class="dash">-</span><span>$ 2,000 - $ 5,000</span></li>
    <li><span>Ice machine</span><span class="dash">-</span><span>$ 1,100</span></li>
  </ul>
</main>
</body>
</html>
```